Adult Literacy Program - flyer to attract volunteers and students

We want a flyer that is engaging, colorful, modern and will appeal to our primary audience of adults aged 40-60. We are trying to attract both prospective volunteers (typically age 50+, mostly women) and students (typically aged 40+).
The flyer should feature diverse people working together in pairs of two, reading or talking, with a workbook or some reading material in front of them.

Our organization trains tutors to work one-on-one with adults who are learning how to read. Most of our adult students are non-native speakers of English. Many are of Haitian or Hispanic origin, so we would like some people who represent that demographic.

The Flyer should represent reading, learning, literacy, knowledge, growth,
and opportunities.
Our students are learning to read so they can advance their job opportunities.

Target Market(s)

Adults aged 40-60, primarily women, retired, volunteers

Industry/Entity Type

Education

Font styles to use
Serif
Sans Serif

Colors

Designer to choose colors to be used in the design.

Requirements
Must have
• - UPDATE: Should be designed as a TRI-FOLD brochure on 8.5 x 11 inch paper that will be folded into thirds.
• - Images of diverse people, women and men, who look Hispanic, Haitian and other nationalities as well as Caucasian.
• - Our logo on the front cover
Nice to have
• The sample flyer is very boring and dry! We are open to different ways of presenting the text.

```html
<!DOCTYPE html>
<html lang="en">
<head>
<meta charset="utf-8">
<title>Volunteer – Enrich a Life</title>
<link href="https://fonts.googleapis.com/css2?family=Lato:wght@400;700;900&display=swap" rel="stylesheet">
<style>
  :root{
    --navy:#1d2868;
    --cyan:#1fa6d6;
    --cyan-light:#3fc1e6;
    --sky:#4fbde6;
    --white:#ffffff;
  }
  html,body{margin:0;padding:0;width:1200px;height:818px;overflow:hidden;background:var(--white);}
  .brochure{position:relative;width:1200px;height:818px;overflow:hidden;font-family:"Lato",sans-serif;color:var(--white);}
  .brochure-shapes{position:absolute;inset:0;}
  .panel-text{position:absolute;text-align:center;}
  .contact-block{left:440px;top:300px;width:420px;}
  .headline{margin:0;font-weight:900;font-size:44px;line-height:1.05;color:var(--navy);}
  .subhead{margin:18px 0 16px;font-weight:900;font-size:25px;line-height:1.1;color:var(--white);}
  .contact-line{margin:0 0 8px;font-size:20px;line-height:1.25;color:var(--white);}
  .contact-email{margin:14px 0 20px;font-weight:900;font-size:20px;color:var(--navy);}
  .web-pill{display:inline-block;background:var(--white);color:var(--navy);font-weight:900;font-size:23px;padding:12px 26px;border-radius:10px;}
  .brand-mark{position:absolute;left:922px;top:177px;width:176px;height:176px;border-radius:50%;background:var(--white);
    display:flex;flex-direction:column;align-items:center;justify-content:center;gap:10px;}
  .brand-dot{width:22px;height:22px;border-radius:50%;background:var(--cyan);}
  .brand-name{width:130px;text-align:center;font-weight:900;font-size:22px;line-height:1.1;color:var(--navy);}
  .volunteer-pill{position:absolute;left:800px;top:388px;width:440px;height:76px;background:var(--white);border-radius:38px 0 0 38px;}
  .volunteer-title{position:absolute;left:835px;top:390px;margin:0;font-weight:900;font-size:56px;line-height:72px;letter-spacing:1px;color:var(--navy);}
  .cover-text{left:850px;top:488px;width:330px;}
  .tagline{margin:0 0 26px;font-size:32px;color:var(--sky);}
  .cover-body{margin:0;font-size:26px;line-height:1.2;color:var(--white);}
</style>
</head>
<body>
<main class="brochure">
  <svg class="brochure-shapes" width="1200" height="818" viewBox="0 0 1200 818">
    <defs>
      <linearGradient id="shelfTones" x1="0" y1="0" x2="1" y2="0.35">
        <stop offset="0" stop-color="#d9dde6"/>
        <stop offset="0.25" stop-color="#7d8fc0"/>
        <stop offset="0.5" stop-color="#b7c5e6"/>
        <stop offset="0.75" stop-color="#8a96b8"/>
        <stop offset="1" stop-color="#c9c2b0"/>
      </linearGradient>
      <radialGradient id="shelfLight" cx="0.55" cy="0.4" r="0.6">
        <stop offset="0" stop-color="#f2e6dc" stop-opacity="0.55"/>
        <stop offset="1" stop-color="#f2e6dc" stop-opacity="0"/>
      </radialGradient>
      <linearGradient id="classroomTones" x1="0" y1="0" x2="1" y2="0.6">
        <stop offset="0" stop-color="#2e2a2c"/>
        <stop offset="0.4" stop-color="#4a5670"/>
        <stop offset="0.7" stop-color="#8f7d6c"/>
        <stop offset="1" stop-color="#e4ddd4"/>
      </linearGradient>
      <radialGradient id="classroomLight" cx="0.6" cy="0.75" r="0.45">
        <stop offset="0" stop-color="#2aa3c8" stop-opacity="0.7"/>
        <stop offset="1" stop-color="#2aa3c8" stop-opacity="0"/>
      </radialGradient>
      <radialGradient id="cyanGlow" cx="0.45" cy="0.5" r="0.7">
        <stop offset="0" stop-color="#3fc1e6"/>
        <stop offset="1" stop-color="#1fa6d6"/>
      </radialGradient>
    </defs>
    <rect width="1200" height="818" fill="#1d2868"/>
    <g role="img" aria-label="Smiling woman holding an open book in front of library shelves">
      <rect x="20" y="26" width="440" height="764" fill="url(#shelfTones)"/>
      <rect x="20" y="26" width="440" height="764" fill="url(#shelfLight)"/>
    </g>
    <path d="M460 0 C395 250 395 560 450 818 L820 818 C860 640 870 460 880 300 L880 0 Z" fill="url(#cyanGlow)"/>
    <path d="M450 818 C395 560 395 250 460 0" fill="none" stroke="#1d2868" stroke-width="18"/>
    <path d="M820 818 C860 640 870 460 900 300 L1200 300 L1200 818 Z" fill="#1d2868"/>
    <g role="img" aria-label="Volunteer tutor helping a smiling adult student at a library table">
      <path d="M500 0 L1200 0 L1200 210 C1120 260 1020 300 900 300 C760 300 600 260 500 0 Z" fill="url(#classroomTones)"/>
      <path d="M500 0 L1200 0 L1200 210 C1120 260 1020 300 900 300 C760 300 600 260 500 0 Z" fill="url(#classroomLight)"/>
    </g>
    <path d="M500 0 C600 260 760 300 900 300 C1020 300 1120 260 1200 210" fill="none" stroke="#1d2868" stroke-width="10"/>
  </svg>

  <div class="brand-mark">
    <span class="brand-dot"></span>
    <span class="brand-name">Open Page Friends</span>
  </div>

  <section class="panel-text contact-block">
    <h2 class="headline">You can make<br>a difference!</h2>
    <p class="subhead">Contact us today<br>to learn more.</p>
    <p class="contact-line">Volunteer Desk: 555-210-4830</p>
    <p class="contact-line">Northfield, Elm Grove &amp; Lake<br>Harbor: 555-374-9162</p>
    <p class="contact-email">email: reading@oakvalelibrary.org</p>
    <span class="web-pill">oakvalelibrary.org/reading</span>
  </section>

  <div class="volunteer-pill"></div>
  <h1 class="volunteer-title">VOLUNTEER</h1>
  <section class="panel-text cover-text">
    <p class="tagline">Enrich a Life!</p>
    <p class="cover-body">Help an adult learn<br>to read, write or<br>speak English</p>
  </section>
</main>
</body>
</html>
```